Dog care service needs business card design

Our company is Pawsome Haven. We provide care for dogs while their owners are away, either through home visits or a holiday stay in the homes of carefully selected minders. Our existing website & Chatterbook cover should provide all the colour cues for our business cards - namely blues, blondes and grey. We have an existing logo (provided).

www.pawsomehaven-demo.com.au
www.facebook.com/pawsomehavenau

We wish to clearly communicate our three areas of service "dog minding, home visits, dog walking".

We would like to have the files ready for upload to Prontoprint (or similar) for immediate printing.

Target Market(s)

Dog owners who love their dogs like family

Industry/Entity Type

Business

Contact Information for Business Card

Pawsome Haven
Ph: 0491 574 318

Font styles to use
Sans Serif

Colors
33a6d7
3176b5

Requirements
Must have
• Logo
• Telephone number
• website
• "Dog minding, home visits, dog walking"
Should not have
• any additional illustrations beyond the logo.

```html
<!DOCTYPE html>
<html lang="en">
<head>
<meta charset="utf-8">
<title>Pawsome Haven – Business Card</title>
<link rel="stylesheet" href="https://fonts.googleapis.com/css2?family=Nunito:wght@400;600;800&display=swap">
<style>
  :root {
    --blue-dark: #3176b5;
    --blue-light: #33a6d7;
    --blue-mid: #2f8cc8;
    --charcoal: #3a3f47;
    --card: #ffffff;
    --stage: #e9ecef;
  }
  * { box-sizing: border-box; margin: 0; padding: 0; }
  html, body {
    width: 1200px; height: 800px; overflow: hidden;
    background: var(--stage);
    font-family: "Nunito", sans-serif;
  }
  .stage {
    position: relative; width: 1200px; height: 800px;
    display: flex; align-items: center; justify-content: center; gap: 40px;
  }
  .card {
    position: relative; width: 540px; height: 330px;
    background: var(--card);
    box-shadow: 0 6px 18px rgba(0,0,0,0.12);
    overflow: hidden;
  }
  .card-shapes { position: absolute; inset: 0; width: 100%; height: 100%; }

  .brand { position: absolute; display: flex; align-items: center; }
  .brand-mark { border-radius: 50%; background: var(--charcoal); flex: none; }
  .brand-name {
    color: var(--blue-dark); font-weight: 800; line-height: 0.95;
  }

  .front .brand { left: 130px; top: 110px; gap: 18px; }
  .front .brand-mark { width: 90px; height: 90px; }
  .front .brand-name { font-size: 44px; }

  .back .brand { right: 30px; top: 132px; gap: 7px; }
  .back .brand-mark { width: 30px; height: 30px; }
  .back .brand-name { font-size: 14px; }

  .services {
    position: absolute; left: 40px; top: 190px;
    color: var(--blue-dark); font-size: 24px; font-weight: 600;
  }
  .contact-list {
    position: absolute; left: 44px; top: 236px; list-style: none;
    color: var(--blue-dark); font-size: 15px; font-weight: 600;
  }
  .contact-list li { display: flex; align-items: center; gap: 10px; margin-bottom: 8px; }
  .contact-list li::before {
    content: ""; width: 8px; height: 8px; background: var(--blue-dark);
  }
</style>
</head>
<body>
<main class="stage">
  <section class="card front" aria-label="Business card front">
    <svg class="card-shapes" viewBox="0 0 540 330" aria-hidden="true">
      <polygon points="0,330 0,150 300,330" fill="var(--blue-dark)"/>
      <polygon points="0,150 0,110 360,330 300,330" fill="var(--blue-light)"/>
      <polygon points="0,330 0,240 150,330" fill="var(--blue-mid)"/>
      <polygon points="540,0 360,0 540,140" fill="var(--blue-dark)"/>
      <polygon points="540,140 540,185 300,0 360,0" fill="var(--blue-light)"/>
      <polygon points="540,0 460,0 540,60" fill="var(--blue-mid)"/>
    </svg>
    <div class="brand">
      <span class="brand-mark"></span>
      <span class="brand-name">Pawsome<br>Haven</span>
    </div>
  </section>

  <section class="card back" aria-label="Business card back">
    <svg class="card-shapes" viewBox="0 0 540 330" aria-hidden="true">
      <polygon points="0,0 540,0 540,40 0,150" fill="var(--blue-light)"/>
      <polygon points="0,0 400,0 0,150" fill="var(--blue-dark)"/>
      <polygon points="0,0 220,0 0,90" fill="var(--blue-mid)"/>
      <line x1="20" y1="176" x2="520" y2="176" stroke="var(--blue-light)" stroke-width="1.5"/>
    </svg>
    <p class="services">Dog minding, home visits, dog walking</p>
    <ul class="contact-list">
      <li>0491 574 318</li>
      <li>www.pawsomehaven-demo.com.au</li>
    </ul>
    <div class="brand">
      <span class="brand-mark"></span>
      <span class="brand-name">Pawsome<br>Haven</span>
    </div>
  </section>
</main>
</body>
</html>
```